Vermilion Reel Works Web Design

COMPANY: VERMILION REEL WORKS
LOCATION: SHANGHAI, CHINA
AREA: FILM/TV DRAMA/COMMERCIALS/GAME POST PRODUCTION, SOUND DESIGN, MUSIC, and GAME.
WEB STYLE: SIMPLE, PROFESSIONAL, TRUSTWORTHY

LANGUAGE: ENGLISH, CHINESE. (Same layout, different language)
UPDATE: AFTER PROJECT FINISHED, WE NEED UPDATE BY OURSELVES.

MAIN SUBJECT: 6
1 HOMEPAGE
2 ABOUT US
3 TEAM
4 SERVICES
5 FACILITY
6 CONTACT

add one page of JOB OPPORTUNITIES.

DETAILS
1 HOMEPAGE
SLOGAN: Vermilion Reel Works provides a well-designed working environment which amplifies your team’s ability to reach their creative goals.

Our services include:
 Feature Films
 Music & Scoring
 Commercials
 ADR & Foley
 Sound & Picture Editorial
 Sound Design
 Video Game

2 ABOUT US
Vermilion Reel Works is located in the premiere South-Bund area of Shanghai. Occupying a 5000 square meter Technical Building, Vermilion Reel Works was built by a filmmaker for filmmakers, and is one of the largest, most versatile full-service post-production facilities in China.

Vermilion Reel Works is positioning to be at the forefront of the latest technology. Our goal is to provide a comprehensive solution for the post-production needs of our clients. We offer two fully-equipped dubbing stages (one of which will be certified KESTRON VOXAR PREMIERE), a large variety of both picture and sound editing rooms, impressive Foley and ADR stages, a world-class scoring stage, and complete audio and video transfer services.

We can handle your entire project from editing all the way to the end of the final sound mix; all under one extremely comfortable roof. We fully realize that the true art is in listening to the needs of our clients and making their greatest vision a reality. To this end our creative team's expertise, with a network of sound supervisors, editors and mixers, will deliver the magic you need. Producers and directors will also find our richly appointed guest accommodations to be a comfortable and soothing place to wind up the day. Every aspect of your project will be taken care of by a skilled and dedicated team, in the way that is best suited to you.

3 TEAM
(attachment 01)

4 SERVICES
Sound Mix
ADR
FOLEY
MUSIC
Sound Design
Sound Edit
Picture Edit
for all the Films, TV Drama, Commercials, Video Games, Online Media
(attachment 02, use photo)

5 FACILITY
(attachment 03)

6 CONTACT
(attachment04)
with map

Project Deadline Extended
Reason: Designers work are great, my bosses will spend 1-2 days select one of these web design, and spend 1-2 days to make some change, maybe use new photos.

```html
<!DOCTYPE html>
<html lang="en">
<head>
<meta charset="utf-8">
<title>Vermilion Reel Works</title>
<link href="https://fonts.googleapis.com/css2?family=Oswald:wght@300;400;500;700&family=Montserrat:wght@400;500&display=swap" rel="stylesheet">
<style>
:root{
  --black:#000;
  --white:#fff;
  --nav-text:#d9d9d9;
  --gold:#a8843a;
  --orange:#f7931e;
  --orange-deep:#f07d00;
  --magenta:#d6136f;
  --hero-purple:#3b1f6e;
  --hero-amber:#b86b1c;
  --hero-olive:#6f6a1a;
}
*{margin:0;padding:0;box-sizing:border-box}
html,body{width:1200px;height:738px;overflow:hidden;background:var(--black)}
.page{position:relative;width:1200px;height:738px;overflow:hidden;font-family:"Oswald",sans-serif;color:var(--white)}

.site-header{position:absolute;left:0;top:0;width:1200px;height:87px;background:var(--black);border-bottom:3px solid var(--gold);z-index:3}
.brand{position:absolute;left:115px;top:14px;font-family:"Oswald",sans-serif;font-weight:500;font-size:40px;line-height:52px;letter-spacing:-0.5px;color:var(--white)}
.main-nav{position:absolute;left:520px;top:29px;display:flex;align-items:center;font-family:"Montserrat",sans-serif;font-weight:500;font-size:13px;letter-spacing:0.6px}
.main-nav a{color:var(--nav-text);text-decoration:none;margin-right:29px;line-height:33px}
.main-nav a.nav-contact{margin-right:0;margin-left:-3px;border:2px solid var(--white);padding:0 22px;color:var(--white);height:34px;line-height:30px}

.hero{position:absolute;left:0;top:90px;width:1200px;height:575px;overflow:hidden}
.hero-photo{position:absolute;inset:0;background:
  linear-gradient(125deg,transparent 52%,rgba(255,215,80,.18) 52%,rgba(255,215,80,.18) 66%,transparent 66%),
  radial-gradient(ellipse at 30% 35%,#6a3a7a 0%,transparent 55%),
  linear-gradient(100deg,var(--hero-purple) 0%,#5a2f5e 25%,var(--hero-amber) 50%,var(--hero-olive) 75%,#4f3a1e 100%)}
.hero-shade{position:absolute;left:0;bottom:0;width:100%;height:220px;background:linear-gradient(transparent,rgba(0,0,0,.55))}
.slogan{position:absolute;right:123px;top:90px;text-align:right;font-weight:300;font-size:27px;line-height:50px;letter-spacing:-0.2px}

.service-label{position:absolute;top:398px;width:156px;height:37px;border:2px solid var(--white);border-radius:3px;background:var(--black);font-size:15px;line-height:33px;text-align:center}
.service-label::after{content:"";position:absolute;left:50%;bottom:-9px;width:12px;height:12px;margin-left:-6px;background:var(--black);border-right:2px solid var(--white);border-bottom:2px solid var(--white);transform:rotate(45deg)}
.service-dial{position:absolute;top:453px;width:148px;height:148px;border-radius:50%;background:radial-gradient(circle,#161616 1px,#050505 1.5px) 0 0/5px 5px,var(--black);border:4px solid var(--white);border-right-color:transparent;display:flex;align-items:center;justify-content:center}
.service-dial svg{width:62px;height:62px;margin-top:-16px}
.nav-arrow{position:absolute;top:589px;width:56px;height:56px;border-radius:50%;border:2px solid var(--white);background:var(--white);box-shadow:inset 0 0 0 3px var(--black);display:flex;align-items:center;justify-content:center;z-index:4}

.featured-service{position:absolute;left:520px;top:508px;width:168px;height:168px;border-radius:50%;background:var(--orange);border:3px solid var(--orange-deep);box-shadow:inset 3px 0 0 2px var(--white);display:flex;align-items:center;justify-content:center;z-index:4;font-weight:700;font-size:29px;letter-spacing:-0.3px}
.featured-service svg{position:absolute;left:50px;top:50px;opacity:.18}
.featured-service span{position:relative}

.site-footer{position:absolute;left:0;top:665px;width:1200px;height:73px;background:var(--black)}
.copyright{position:absolute;left:115px;top:32px;font-weight:300;font-size:17px;letter-spacing:0.2px}
.get-in-touch{position:absolute;left:810px;top:28px;font-weight:300;font-size:17px;color:#cfcfcf;letter-spacing:0.4px}
.social{position:absolute;top:23px;width:35px;height:35px;border-radius:50%;background:var(--white);color:var(--black);font-family:"Oswald",sans-serif;font-weight:400;font-size:14px;line-height:35px;text-align:center;text-decoration:none}
</style>
</head>
<body>
<div class="page">
  <header class="site-header">
    <div class="brand">VERMILION REEL WORKS</div>
    <nav class="main-nav">
      <a href="#">HOMEPAGE</a>
      <a href="#">ABOUT US</a>
      <a href="#">TEAM</a>
      <a href="#">SERVICES</a>
      <a href="#">FACILITY</a>
      <a href="#" class="nav-contact">CONTACT</a>
    </nav>
  </header>

  <section class="hero">
    <div class="hero-photo" role="img" aria-label="Sound engineer seated at a mixing console in a post-production suite, tinted purple and amber"></div>
    <div class="hero-shade"></div>
    <p class="slogan">Vermilion Reel Works Provides A Well-designed Working Environment Which Amplifies<br>Your Team’s Ability To Reach Their Creative Goals.</p>

    <div class="service-label" style="left:153px">Sound &amp; Picture Editorial</div>
    <div class="service-label" style="left:339px">Music &amp; Scoring</div>
    <div class="service-label" style="left:723px">Video Game</div>
    <div class="service-label" style="left:893px">Sound Design</div>

    <div class="service-dial" style="left:160px">
      <svg viewBox="0 0 60 60" fill="none" stroke="#fff" stroke-width="5"><rect x="4" y="8" width="52" height="44"/><circle cx="37" cy="22" r="5"/><path d="M8 48 L24 30 L36 42 L44 36 L52 46" stroke-linejoin="round"/></svg>
    </div>
    <div class="service-dial" style="left:342px">
      <svg viewBox="0 0 60 60" fill="none" stroke="#fff" stroke-width="5" stroke-linecap="round"><path d="M4 12 H34 M4 24 H34 M4 36 H26 M4 48 H26"/><path d="M46 6 V46"/><circle cx="40" cy="47" r="7"/><path d="M46 6 Q56 8 56 18"/></svg>
    </div>
    <div class="service-dial" style="left:711px">
      <svg viewBox="0 0 60 60" fill="none" stroke="#fff" stroke-width="5" stroke-linejoin="round"><path d="M54 6 C40 6 28 14 20 30 L30 40 C46 32 54 20 54 6 Z"/><circle cx="40" cy="20" r="4"/><path d="M20 30 L10 30 L18 20 L28 20 M30 40 L30 50 L40 42 L40 32"/><path d="M16 40 L6 54 L20 44"/></svg>
    </div>
    <div class="service-dial" style="left:893px">
      <svg viewBox="0 0 60 60" fill="none" stroke="#fff" stroke-width="5" stroke-linejoin="round"><path d="M20 46 V12 L54 4 V38"/><path d="M20 20 L54 12"/><circle cx="13" cy="47" r="7"/><circle cx="47" cy="39" r="7"/></svg>
    </div>
  </section>

  <div class="nav-arrow" style="left:57px" aria-label="Previous">
    <svg width="32" height="32" viewBox="0 0 32 32" fill="none" stroke="#d6136f" stroke-width="3" stroke-linecap="round" stroke-linejoin="round"><circle cx="16" cy="16" r="13"/><path d="M23 16 H10 M15 10 L9 16 L15 22"/></svg>
  </div>
  <div class="nav-arrow" style="left:1079px" aria-label="Next">
    <svg width="32" height="32" viewBox="0 0 32 32" fill="none" stroke="#d6136f" stroke-width="3" stroke-linecap="round" stroke-linejoin="round"><circle cx="16" cy="16" r="13"/><path d="M9 16 H22 M17 10 L23 16 L17 22"/></svg>
  </div>

  <div class="featured-service">
    <svg width="64" height="60" viewBox="0 0 64 60" fill="none" stroke="#fff" stroke-width="5"><path d="M4 28 L32 6 L60 28 M12 24 V56 H52 V24"/></svg>
    <span>COMMERCIALS</span>
  </div>

  <footer class="site-footer">
    <p class="copyright">COPYRIGHT 2014 | VERMILION REEL WORKS  PVT. LTD. 2014</p>
    <span class="get-in-touch">GET IN TOUCH :</span>
    <a class="social" href="#" style="left:916px">Qi</a>
    <a class="social" href="#" style="left:958px">Nu</a>
    <a class="social" href="#" style="left:1001px">Zo</a>
    <a class="social" href="#" style="left:1044px">Ek</a>
  </footer>
</div>
</body>
</html>
```